Professional Learning Organization for Educators needs a Design Thinking Workshop Flyer

We need a flyer for a series of Introductory Design Thinking workshops we're delivering for education leaders.

We have generated our own version of the flyer with a word template, but want it to look even more professional and eye catching. It is attached.

We had an image that we thought might be good, but pulled it out so we don't bias designers' thinking.
Updates

Reason: We are a bit flexible on the deadline since this is a holiday week and people are traveling

Target Market(s)

Very busy education leaders whose curiosity needs to be stimulated enough to enroll in the course

Industry/Entity Type

Education

Font styles to use
Other font styles liked:
• Century Gothic or something closer to that

Requirements
Must have
• Some version of the text that is on the current flyer that I attached.
Nice to have
• I am very flexible and open right now on this design.

```html
<!DOCTYPE html>
<html lang="en">
<head>
<meta charset="utf-8">
<title>Design Thinking Workshops Flyer</title>
<link rel="stylesheet" href="https://fonts.googleapis.com/css2?family=Roboto+Condensed:wght@400;700&family=Mulish:wght@800&family=Open+Sans:wght@600&family=Questrial&display=swap">
<style>
  :root {
    --page: #ececec;
    --paper: #ffffff;
    --orange: #e8820f;
    --orange-deep: #c9580a;
    --orange-text: #d9700f;
    --yellow-text: #ffe23a;
    --green: #6cc811;
    --green-pale: #d6e9b4;
    --red: #e81b12;
    --note: #fbe75a;
    --note-edge: #f4d63c;
    --pin: #d11a12;
    --navy: #2e4a8a;
    --slate: #3e5c8c;
    --grey-panel: #efefef;
    --board: #3a4440;
  }
  * { box-sizing: border-box; margin: 0; padding: 0; }
  html, body { width: 1200px; height: 1200px; overflow: hidden; background: var(--page); }
  .flyer {
    position: absolute; left: 189px; top: 20px;
    width: 970px; height: 1370px;
    transform: scale(0.8467); transform-origin: top left;
    background: var(--paper); overflow: hidden;
    box-shadow: 0 8px 24px rgba(0,0,0,.18);
    font-family: "Roboto Condensed", "Arial Narrow", sans-serif;
  }
  .abs { position: absolute; }
  .hero-art { left: 0; top: 0; }
  .quotes-banner {
    left: 548px; top: 0; width: 422px; height: 80px;
    background: var(--red);
    clip-path: polygon(0 0, 100% 0, 100% 100%, 80px 100%);
    color: #fff; font-family: "Mulish", sans-serif; font-weight: 800;
    font-size: 25px; line-height: 29px; text-align: center;
    padding: 17px 0 0 70px; letter-spacing: .3px;
  }
  .note-backdrop {
    left: 535px; top: 650px; width: 470px; height: 330px;
    background: var(--grey-panel); border-radius: 60px 0 0 40px;
    clip-path: polygon(110px 0, 100% 0, 100% 100%, 0 100%, 0 260px);
  }
  .note {
    width: 292px; height: 190px;
    background: linear-gradient(160deg, var(--note) 60%, var(--note-edge));
    box-shadow: 3px 6px 10px rgba(0,0,0,.2);
    font-family: "Open Sans", sans-serif; font-weight: 600;
    color: #3a3320; font-size: 17.5px; line-height: 26px; text-align: center;
    display: flex; flex-direction: column; justify-content: center; padding: 10px 22px;
  }
  .note .pin {
    position: absolute; width: 24px; height: 24px; border-radius: 50%;
    background: radial-gradient(circle at 35% 35%, #ff6a5e, var(--pin) 60%, #8a0c07);
  }
  .note-1 { left: 654px; top: 100px; transform: rotate(-3deg); }
  .note-1 .pin { right: 10px; top: -8px; }
  .note-2 { left: 655px; top: 318px; transform: rotate(4deg); }
  .note-2 .pin { left: 18px; top: -6px; }
  .note-3 { left: 655px; top: 538px; transform: rotate(-4deg); }
  .note-3 .pin { right: 10px; top: -8px; }
  .note-4 { left: 655px; top: 752px; transform: rotate(3deg); }
  .note-4 .pin { left: 18px; top: -6px; }
  .note-4 p + p { margin-top: 22px; }

  .intro-panel {
    left: 0; top: 512px; width: 640px; height: 470px;
    background: linear-gradient(90deg, #e47a0c, var(--orange) 60%, #ef8f14);
    border-radius: 0 60px 0 0;
    clip-path: polygon(0 0, 100% 0, 96% 20%, 83% 68%, 74% 88%, 63% 100%, 0 100%);
  }
  .band { position: absolute; left: 0; right: 0; background: rgba(170,70,0,.28); }
  .intro-title {
    left: 24px; top: 522px; color: #fff; font-weight: 700; font-size: 45px; letter-spacing: .2px;
  }
  .intro-sub {
    left: 27px; top: 584px; color: var(--yellow-text); font-weight: 700; font-size: 29px;
  }
  .intro-copy {
    left: 26px; top: 630px; width: 545px; color: #fff; font-size: 19px; line-height: 26px;
  }
  .intro-point {
    left: 24px; color: var(--yellow-text); font-weight: 700; font-size: 22px; line-height: 26px;
  }

  .schedule-lead {
    left: 30px; top: 1018px; width: 910px; text-align: center;
    color: var(--navy); font-size: 23px; line-height: 30px; letter-spacing: .2px;
  }
  .session {
    width: 450px; height: 58px; text-align: center;
    font-family: "Mulish", sans-serif; font-weight: 800; color: var(--orange-text);
    font-size: 21px; line-height: 25px; letter-spacing: .5px;
    background: linear-gradient(#fff, #f6f6f6);
    box-shadow: 0 6px 8px -4px rgba(0,0,0,.12);
    padding-top: 4px;
  }
  .grid-line { background: #a8b4cc; }

  .footer-enrol {
    left: 0; top: 1278px; width: 500px; height: 92px;
    background: linear-gradient(90deg, var(--orange-deep), var(--orange));
    clip-path: polygon(0 0, 400px 0, 490px 100%, 0 100%);
    color: #fff; font-size: 19px; padding: 18px 0 0 24px; line-height: 32px;
  }
  .footer-enrol strong { font-size: 25px; font-weight: 700; }
  .footer-fees {
    left: 400px; top: 1278px; width: 570px; height: 92px;
    background: var(--slate);
    clip-path: polygon(0 0, 100% 0, 100% 100%, 90px 100%);
    color: #fff; font-family: "Questrial", sans-serif;
    font-size: 20px; line-height: 24px; text-align: right; padding: 8px 22px 0 0;
  }
</style>
</head>
<body>
<main class="flyer">
  <svg class="abs hero-art" width="970" height="620" viewBox="0 0 970 620">
    <path d="M0 0 H560 C548 150 560 300 820 510 C700 470 560 470 380 510 C220 520 90 520 0 520 Z" fill="var(--green-pale)"/>
    <path d="M0 0 H545 C530 150 540 300 780 500 C650 450 520 445 360 480 C210 500 90 500 0 480 Z" fill="var(--green)"/>
    <path d="M0 0 H470 C455 140 470 270 520 420 C400 390 290 372 200 378 C110 384 50 395 0 410 Z"
          fill="var(--board)" role="img" aria-label="Photo: a thoughtful child beside a chalk light bulb drawing on a green chalkboard"/>
    <path d="M840 495 C820 530 830 560 850 580" stroke="var(--green)" stroke-width="2" fill="none"/>
  </svg>

  <div class="abs quotes-banner">WHAT OUR<br>PARTICIPANTS SAY...</div>

  <div class="abs note-backdrop"></div>

  <div class="abs note note-1"><span class="pin"></span>“This has been an empowering experience that allowed me to try out dramatic changes in my practice that I wouldn’t have imagined before.”</div>
  <div class="abs note note-2"><span class="pin"></span>“I never realized how often I’ve guessed and assumed what our teachers and students need – now I have a way to stop guessing!”</div>
  <div class="abs note note-3"><span class="pin"></span>“I finally have tools to generate truly creative ideas that people actually embrace… because they meet their needs”</div>
  <div class="abs note note-4"><span class="pin"></span><p>SUMMIT VALLEY CO-OP<br>www.svcoop.org</p><p>Questions?<br>j.ellis@svcoop.org</p></div>

  <div class="abs intro-panel">
    <div class="band" style="top:72px;height:44px"></div>
    <div class="band" style="top:326px;height:84px"></div>
    <div class="band" style="top:412px;height:4px;background:rgba(255,255,255,0)"></div>
    <div class="band" style="top:460px;height:10px"></div>
  </div>
  <h1 class="abs intro-title">DESIGN THINKING WORKSHOPS</h1>
  <h2 class="abs intro-sub">Designing your way to better solutions.</h2>
  <p class="abs intro-copy">Maple Ridge Public Schools and Summit Valley Co-op invite you to discover the power of Design Thinking. During our three session course, you will learn and practice mindsets and tools that help you continuously and creatively improve the experiences of the people you serve by :</p>
  <p class="abs intro-point" style="top:752px;width:520px">Understanding what your teachers, students and community truly need in their learning and work experiences</p>
  <p class="abs intro-point" style="top:858px">Designing solutions that better meet their needs</p>
  <p class="abs intro-point" style="top:905px;width:480px">Seeking authentic feedback and reactions to these solutions prior to their implementation.</p>

  <p class="abs schedule-lead">WE ARE OFFERING THIS THREE-SESSION COURSE AT FOUR DIFFERENT TIMES IN SPRING SEMESTER.&nbsp; PLEASE CHOOSE THE COURSE THAT WORKS BEST FOR YOUR SCHEDULE.</p>

  <div class="abs grid-line" style="left:485px;top:1098px;width:2px;height:160px"></div>
  <div class="abs grid-line" style="left:25px;top:1175px;width:920px;height:2px"></div>
  <div class="abs session" style="left:25px;top:1098px">MONDAY MORNINGS<br>23RD &amp; 30TH JAN AND 6TH FEB</div>
  <div class="abs session" style="left:492px;top:1100px">TUESDAY&nbsp; AFTERNOONS<br>7TH, 14TH &amp; 21ST FEB</div>
  <div class="abs session" style="left:25px;top:1195px">WEDNESDAY AFTERNOONS<br>8TH, 15TH &amp; 22ND MAR</div>
  <div class="abs session" style="left:492px;top:1195px">WEDNESDAY EVENINGS<br>8TH, 15TH &amp; 22ND FEB</div>

  <div class="abs footer-enrol">Click here to enroll .<br>Go to <strong>www.svcoop.org</strong> to learn more.</div>
  <div class="abs footer-fees">This course is held in Maple Ridge Public Schools.<br>No fee for MRPS leaders.<br>$150 fee for leaders outside of MRPS.</div>
</main>
</body>
</html>
```